OLU58 biz card & Stationery

LU58 is a personalized shopping experience brought to you, that lets you find and discover fashion goods through a collection of boutiques curated by taste-makers - celebrities, stylists, designers, and fashion bloggers. Boutiques uses visual technology to help fashionistas discover and shop their look and creates the opportunity for designers to showcase their collections and latest inspirations online.

OLU58 is built on technology developed by our team of fashion experts who work with engineers to “teach” our computer systems to understand various patterns, pairings, and genre definitions. When signed into your account, OLU58 learns about your style and preferences and in turn, provides you better results and recommendations over time. Ultimately, OLU58 will provide shoppers with a much richer and interactive shopping experience and help drive traffic to retailers' websites.

We need a definitely cool business card. The card must be black! And must use our official logo which can be download from OLU58.com

The address for Letter head and evenlop, please use 4872 Crestwick Parkway, Sutie 510 Los Angeles CA90412, email will be anyone@OLU58.com, website is www.OLU58.com

thanks

We received some of the design, thanks. But most of the design are not what we want. We need a very clean version with black ground, you may also use some dark gray to add the element. please take a look at http://morvalstudio.no/work/#pelter__ostrama/, we do like this kind of design very much. hope it help.

```html
<!DOCTYPE html>
<html lang="en">
<head>
<meta charset="utf-8">
<title>OLU58 Stationery</title>
<link href="https://fonts.googleapis.com/css2?family=Questrial&display=swap" rel="stylesheet">
<style>
:root{
  --bg:#e9e6e2;
  --ink:#2a2727;
  --ink-deep:#221f1f;
  --band:#4d4b4b;
  --paper:#ffffff;
  --text-light:#e6e6e6;
  --text-dim:#a9a9a9;
  --photo-light-a:#f6f6f6;
  --photo-light-b:#e2e2e2;
  --photo-dark-a:#4a4848;
  --photo-dark-b:#2e2b2b;
}
*{margin:0;padding:0;box-sizing:border-box}
html,body{width:1200px;height:900px;overflow:hidden}
body{background:var(--bg);font-family:"Questrial",sans-serif;position:relative}
.piece{position:absolute;box-shadow:0 2px 6px rgba(0,0,0,.25)}
.wordmark{font-weight:400;color:var(--text-light);line-height:1;letter-spacing:2px;white-space:nowrap}
.descriptor{color:var(--text-dim);letter-spacing:1.5px;text-transform:uppercase;line-height:1;white-space:nowrap}
.icon{width:8px;height:8px;vertical-align:-1px;margin-right:3px;fill:var(--text-light)}

/* Letterhead */
.letterhead{left:30px;top:108px;width:516px;height:730px;background:var(--paper)}
.letterhead .header{position:absolute;left:0;top:0;width:100%;height:68px;background:var(--ink)}
.letterhead .header-band{position:absolute;left:0;top:68px;width:100%;height:10px;background:var(--band)}
.letterhead .wordmark{position:absolute;left:20px;top:18px;font-size:26px}
.letterhead .descriptor{position:absolute;left:20px;top:50px;font-size:7.5px}
.letterhead .contact{position:absolute;left:369px;top:12px;font-size:7.5px;color:var(--text-light);line-height:10px}
.letterhead .contact .gap{height:4px}
.letterhead .photo{position:absolute;left:0;top:290px;width:430px;height:430px;background:radial-gradient(ellipse at 50% 45%,var(--photo-light-b) 0%,var(--photo-light-a) 55%,var(--paper) 80%)}
.letterhead .footer{position:absolute;left:0;bottom:0;width:100%;height:10px;background:var(--ink-deep)}
.letterhead .footer span{position:absolute;right:8px;top:0;font-size:8px;line-height:10px;letter-spacing:1.5px;color:var(--text-light)}

/* Business cards */
.card{top:135px;width:219px;height:124px;background:var(--ink)}
.card-front{left:646px}
.card-front .wordmark{position:absolute;right:12px;top:12px;font-size:23px}
.card-front .descriptor{position:absolute;right:12px;top:41px;font-size:6.5px}
.card-front .name{position:absolute;left:12px;top:65px;font-size:9px;color:var(--text-light)}
.card-front .details{position:absolute;top:94px;font-size:5px;line-height:6.5px;color:var(--text-dim)}
.card-front .details.address{left:12px}
.card-front .details.lines{left:112px}
.card-front .details .icon{width:5px;height:5px;margin-right:2px;fill:var(--text-dim)}
.card .bottom-band{position:absolute;left:0;bottom:0;width:100%;height:6px;background:var(--band)}
.card-back{left:884px;background:linear-gradient(90deg,var(--ink) 0%,var(--ink-deep) 100%)}
.card-back .photo{position:absolute;left:0;top:0;width:100px;height:100%;background:linear-gradient(180deg,var(--photo-dark-a) 0%,var(--photo-dark-b) 100%)}
.card-back .wordmark{position:absolute;right:18px;top:49px;font-size:18px}
.card-back .descriptor{position:absolute;right:18px;top:72px;font-size:5.5px}
.card-back .web{position:absolute;right:28px;bottom:3px;font-size:5px;letter-spacing:1px;color:var(--text-dim)}

/* Envelope front */
.envelope-front{left:578px;top:283px;width:593px;height:257px;background:linear-gradient(90deg,var(--ink-deep) 0%,var(--ink-deep) 55%,var(--ink) 100%)}
.envelope-front .wordmark{position:absolute;left:20px;top:20px;font-size:30px}
.envelope-front .descriptor{position:absolute;left:20px;top:56px;font-size:9px}
.envelope-front .address{position:absolute;left:20px;top:72px;font-size:6.5px;color:var(--text-light)}
.envelope-front .photo{position:absolute;left:390px;top:0;width:203px;height:244px;background:linear-gradient(90deg,rgba(74,72,72,0) 0%,var(--photo-dark-a) 35%,var(--photo-dark-b) 100%)}
.envelope-front .bottom-band{position:absolute;left:0;bottom:0;width:100%;height:13px;background:var(--band)}
.envelope-front .web{position:absolute;right:8px;bottom:2px;font-size:8px;letter-spacing:1.5px;color:var(--text-light)}

/* Envelope back */
.envelope-back{left:578px;top:560px;width:593px;height:257px;background:var(--ink-deep)}
.envelope-back svg{position:absolute;left:0;top:0}
</style>
</head>
<body>

<section class="piece letterhead">
  <div class="header">
    <div class="wordmark">OLU58</div>
    <div class="descriptor">Curated Boutiques</div>
    <div class="contact">
      <div>4872 Crestwick Pkwy,</div>
      <div>Sutie 510 Los Angeles CA90412</div>
      <div class="gap"></div>
      <div><svg class="icon" viewBox="0 0 10 10"><path d="M1 3h8v2l-2 1v-1H3v1L1 5z M2 6h6v3H2z"/></svg>: 1300 482 917</div>
      <div><svg class="icon" viewBox="0 0 10 10"><rect x="3" y="0" width="4" height="10" rx="1"/></svg>: 40018273564</div>
      <div><svg class="icon" viewBox="0 0 10 10"><path d="M0 2h10v6H0z M1 3l4 3 4-3" fill="none" stroke="#e6e6e6"/></svg>: nadia@OLU58.com</div>
    </div>
  </div>
  <div class="header-band"></div>
  <div class="photo" role="img" aria-label="Faded black and white portrait of a fashion model as a watermark"></div>
  <div class="footer"><span>www.OLU58.com</span></div>
</section>

<section class="piece card card-front">
  <div class="wordmark">OLU58</div>
  <div class="descriptor">Curated Boutiques</div>
  <div class="name">Nadia Halvorsen</div>
  <div class="details address">
    <div>4872 Crestwick Pkwy,</div>
    <div>Sutie 510 Los Angeles CA90412,</div>
    <div>W : www.OLU58.com</div>
  </div>
  <div class="details lines">
    <div><svg class="icon" viewBox="0 0 10 10"><path d="M1 3h8v2l-2 1v-1H3v1L1 5z M2 6h6v3H2z"/></svg>: 1300 482 917</div>
    <div><svg class="icon" viewBox="0 0 10 10"><rect x="3" y="0" width="4" height="10" rx="1"/></svg>: 40018273564</div>
    <div><svg class="icon" viewBox="0 0 10 10"><rect x="0" y="2" width="10" height="6"/></svg>: nadia@OLU58.com</div>
  </div>
  <div class="bottom-band"></div>
</section>

<section class="piece card card-back">
  <div class="photo" role="img" aria-label="Black and white photo of a fashion model in a cardigan"></div>
  <div class="wordmark">OLU58</div>
  <div class="descriptor">Curated Boutiques</div>
  <div class="web">www.OLU58.com</div>
</section>

<section class="piece envelope-front">
  <div class="wordmark">OLU58</div>
  <div class="descriptor">Curated Boutiques</div>
  <div class="address">4872 Crestwick Pkwy, Sutie 510 LA CA90412</div>
  <div class="photo" role="img" aria-label="Toned black and white photo of a fashion model standing with hand on hip"></div>
  <div class="bottom-band"></div>
  <div class="web">www.OLU58.com</div>
</section>

<section class="piece envelope-back">
  <svg width="593" height="257" viewBox="0 0 593 257" aria-hidden="true">
    <path d="M2 2 C6 40 14 66 42 72 L297 106 L551 72 C579 66 587 40 591 2" fill="none" stroke="#6a6767" stroke-width="1"/>
    <path d="M150 87 L10 250 M444 87 L583 250" fill="none" stroke="#6a6767" stroke-width="1"/>
  </svg>
</section>

</body>
</html>
```